Financial Advisor Resource Firm needs business card design

Need business card design for company in Omaha NE called Tallowbrook Partners. We provide resources to financial advisors....workshop programs, retirement analysis, and insurance planning. I would like to see designs that use grays, greens, black, and white colors. The final design should communicate 'collaboration' and be simple yet attractive to financial planning clients. I will attached our logo and another picture of a puzzle piece coming together. I would like the incorporate the puzzle picture somehow, maybe on the back somehow, with color or just the gray scale....OR, the picture be the front of the card with 'Tallowbrook' definition on it (see upload) and then company logo, employee name, title, address on the back (see ppt uploaded). The following disclosure needs to be included somewhere- Advisory services offered through Marlowe Ridge Advisors, LLC.
Updates

I uploaded a svg and ai file of the logo

Target Market(s)

Financial planning clients and financial advisors....so pretty diverse age range of about 40-70.

Industry/Entity Type

Financial Planning

Contact Information for Business Card

Dennis K. Holloway, MBA
Founder/President
5727 E. Larkspur Avenue
Suite 418
Omaha, NE 68297
Phone- (402) 555-0147
Cell- (402) 555-0183
Fax- (402) 555-0129
email- dennis@tallowbrookgroup.example
web address- www.tallowbrookgroup.example

Colors
1b1b1b
474747
d3d3d3
ffffff
9bcb3c
abd036

Requirements
Must have
• Must include logo provided, must be 2 sided, and must have disclosure...all of these items listed in project description

```html
<!DOCTYPE html>
<html lang="en">
<head>
<meta charset="utf-8">
<title>Tallowbrook Partners — Business Card</title>
<link rel="stylesheet" href="https://fonts.googleapis.com/css2?family=Alegreya+Sans:wght@400;500;700&family=Cinzel:wght@400&display=swap">
<style>
  :root {
    --backdrop: #c4c4c4;
    --ink: #060606;
    --charcoal: #1b1b1b;
    --slate: #474747;
    --mist: #d3d3d3;
    --white: #ffffff;
    --green: #9bcb3c;
    --green-deep: #8cc13a;
  }
  * { margin: 0; padding: 0; box-sizing: border-box; }
  html, body { width: 1200px; height: 1200px; overflow: hidden; }
  body {
    background: var(--backdrop);
    font-family: "Alegreya Sans", sans-serif;
    position: relative;
  }
  .card {
    position: absolute;
    left: 191px;
    width: 820px;
    height: 470px;
    overflow: hidden;
    box-shadow: 0 3px 8px rgba(0,0,0,0.25);
  }
  /* Front */
  .card-front { top: 105px; }
  .front-photo {
    position: absolute; inset: 0;
    background:
      radial-gradient(ellipse at 25% 20%, rgba(200,200,200,0.55), transparent 55%),
      radial-gradient(ellipse at 70% 75%, rgba(30,30,30,0.7), transparent 60%),
      linear-gradient(135deg, #8a8a8a 0%, #5c5c5c 45%, #2e2e2e 100%);
  }
  .definition {
    position: absolute; left: 0; right: 0; top: 180px;
    text-align: center; color: var(--white);
  }
  .definition-word {
    font-family: "Cinzel", serif;
    font-size: 62px; line-height: 1;
    color: var(--green);
    letter-spacing: 1px;
  }
  .definition-phonetic {
    font-size: 32px; margin-top: 12px; line-height: 1;
  }
  .definition-meaning {
    font-size: 19px; margin-top: 18px; letter-spacing: 0.2px;
  }
  /* Back */
  .card-back { top: 614px; height: 468px; background: var(--ink); }
  .brand {
    position: absolute; right: 30px; top: 58px;
    display: flex; align-items: center; gap: 14px;
    color: var(--white);
    font-weight: 700; font-size: 36px; line-height: 1.05;
    text-align: right; letter-spacing: 1px;
  }
  .brand-dot {
    width: 22px; height: 22px; border-radius: 50%;
    background: var(--green);
  }
  .person { position: absolute; left: 30px; top: 168px; }
  .person-name { color: var(--white); font-weight: 700; font-size: 25px; line-height: 1; }
  .person-title { color: var(--green); font-size: 19px; margin-top: 6px; letter-spacing: 0.3px; }
  .person-rule { width: 60px; height: 3px; background: var(--white); margin-top: 6px; }
  .contacts {
    position: absolute; left: 30px; top: 252px;
    list-style: none; color: var(--white);
    font-size: 19.5px; line-height: 23px; letter-spacing: 0.4px;
  }
  .contacts li { display: flex; align-items: center; gap: 12px; }
  .contacts svg { width: 14px; height: 14px; fill: var(--green); flex: none; }
  .address {
    position: absolute; right: 30px; top: 274px;
    color: var(--white); text-align: right;
    font-size: 19.5px; line-height: 23px; letter-spacing: 0.4px;
  }
  .wave { position: absolute; left: 0; bottom: 0; width: 820px; height: 468px; }
  .disclosure {
    position: absolute; right: 30px; bottom: 27px;
    color: var(--white); text-align: right;
    font-weight: 700; font-size: 19px; line-height: 24px; letter-spacing: 0.3px;
  }
</style>
</head>
<body>

<section class="card card-front">
  <div class="front-photo" role="img" aria-label="Grayscale photo of many hands joining puzzle pieces together"></div>
  <div class="definition">
    <div class="definition-word">TALLOW·BROOK</div>
    <div class="definition-phonetic">ˈta-lō-ˌbru̇k</div>
    <div class="definition-meaning">: to come together and unite in common interest and focus</div>
  </div>
</section>

<section class="card card-back">
  <div class="brand">
    <span class="brand-dot"></span>
    <span>TALLOWBROOK<br>PARTNERS</span>
  </div>

  <div class="person">
    <div class="person-name">Dennis K. Holloway, MBA</div>
    <div class="person-title">Founder/President</div>
    <div class="person-rule"></div>
  </div>

  <ul class="contacts">
    <li><svg viewBox="0 0 14 14"><path d="M4 0h6a1 1 0 0 1 1 1v12a1 1 0 0 1-1 1H4a1 1 0 0 1-1-1V1a1 1 0 0 1 1-1zm.5 1.5v9.5h5V1.5zM7 11.6a.8.8 0 1 0 0 1.6.8.8 0 0 0 0-1.6z"/></svg>(402) 555-0183</li>
    <li><svg viewBox="0 0 14 14"><path d="M3 1l2.2 2.6-1.2 1.6c.9 1.9 2.2 3.2 4 4l1.6-1.2L12.2 10 11 12.5C5.5 12 2 8.5 1.5 3z"/></svg>(402) 555-0147</li>
    <li><svg viewBox="0 0 14 14"><path d="M3.5 0h7v4h-7zM1 5h12v6h-2.5V9h-7v2H1zM4.5 10h5v4h-5z"/></svg>(402) 555-0129</li>
    <li><svg viewBox="0 0 14 14"><path d="M0 3h14v1.2L7 8.5 0 4.2zM0 5.6l7 4.3 7-4.3V12H0z"/></svg>dennis@tallowbrookgroup.example</li>
    <li><svg viewBox="0 0 14 14"><path d="M7 0a7 7 0 1 0 0 14A7 7 0 0 0 7 0zm0 1.3c.8.9 1.4 2.4 1.6 4.1H5.4C5.6 3.7 6.2 2.2 7 1.3zM1.4 6.6h2.8c0 1.7.4 3.2 1 4.4a5.7 5.7 0 0 1-3.8-4.4zm0-1.2a5.7 5.7 0 0 1 3.8-4.4c-.6 1.2-1 2.7-1 4.4zm4 1.2h3.2C8.5 8.4 7.9 10 7 10.9 6.1 10 5.5 8.4 5.4 6.6zm4.4 0h2.8a5.7 5.7 0 0 1-3.8 4.4c.6-1.2 1-2.7 1-4.4zm0-1.2c0-1.7-.4-3.2-1-4.4a5.7 5.7 0 0 1 3.8 4.4z"/></svg>www.tallowbrookgroup.example</li>
  </ul>

  <div class="address">5727 E. Larkspur Avenue, Suite 418<br>Omaha, NE 68297</div>

  <svg class="wave" viewBox="0 0 820 468" aria-hidden="true">
    <path fill="var(--green-deep)" d="M0,386 C240,412 520,330 820,356 L820,468 L0,468 Z"/>
    <path fill="var(--ink)" d="M0,396 C250,420 500,350 740,356 C480,356 260,420 0,412 Z"/>
    <path fill="var(--white)" d="M0,408 C230,440 480,366 700,357 C460,368 240,446 0,428 Z"/>
  </svg>

  <div class="disclosure">Advisory services offered through<br>Marlowe Ridge Advisors, LLC</div>
</section>

</body>
</html>
```